Graphic Design Project

We are a new business, Silver Fern Gatherings, specialising in organising and holding professional development retreats in exotic locations (generally outside Australia.) We are targeting professionals and practitioners in the health-related industries (e.g. psychologists, doctors, healing practitioners.)

I need a small brochure (either 3-fold A4 size) or double-sided A4 to promote a retreat we are organising in Bali next year (Bali Harvest & Stillness). This retreat focuses on the 3 practices of Buddhism (Nicheren), Mindfulness and Hypnosis, and introduces newcomers to each of these practices. Nichiren Buddhism embraces the practice of chanting (Nam myho ho renge kyo)

We would like the brochure to strike the right balance between visual (nice pictures of Bali and the retreat location at Coral Pond Lodges, Bali) and descriptive text content which will give enough information to busy health professionals and appeal to their professional development needs (see attached content draft.)
Updates

Target Market(s)

health care professionals (e.g. clinical psychologists, mental health professionals, doctors, lawyers and anyone in the mental healthcare industries.

Industry/Entity Type

Health

Requirements
Must have
• visuals showing aspects of: Nichiren Buddhism (chanting or hands together with beads pose), massage, contemplation, mindfulness etc, plus images showing retreat location (Coral Pond Lodges, Bali). There is a lot of material on the latter's website.
A symbol of Nichiren Buddhism is the lotus flower NOT Buddha.

Colours should be restful and muted.

Ages of people targeted are between 30 and 60.

Follow the Copy draft loosely but feel free to re-arrange the elements to fit the brochure/flyer format

Logo/text style for SILVER FERN GATHERINGS optional. (We don't currently have a logo).

Images are representative only.
Nice to have
• Good (similar) sites that we admire are:
www.islandtidewell.com.au
http://www.brightmoorlearning.com.au/workshop-in-bali/bali2013.html
Should not have
• avoid design cliches
No yoga poses
No images of Buddha (Nichiren Buddhism is a humanistic belief system so there is no worship of Buddha himself).
Lotus flower more appropriate.

```html
<!DOCTYPE html>
<html lang="en">
<head>
<meta charset="utf-8">
<title>Silver Fern Gatherings – Bali Harvest &amp; Stillness flyer</title>
<link href="https://fonts.googleapis.com/css2?family=Open+Sans:wght@400;600;700;800&family=Noto+Sans:wght@400;700&display=swap" rel="stylesheet">
<style>
  :root{
    --stage:#262626;
    --orange:#f7941d;
    --orange-deep:#f26522;
    --red:#a20f12;
    --ink:#1a1a1a;
    --white:#ffffff;
    --label:#e6e6e6;
  }
  *{margin:0;padding:0;box-sizing:border-box}
  html,body{width:1200px;height:1000px;overflow:hidden;background:var(--stage)}
  body{position:relative;font-family:"Open Sans",Arial,sans-serif;color:var(--ink)}
  .panel{position:absolute;top:92px;height:836px;overflow:hidden}
  .front{left:8px;width:592px;background:var(--orange)}
  .back{left:604px;width:588px;background:var(--orange-deep)}
  .side-label{position:absolute;top:935px;font-family:"Noto Sans",sans-serif;font-size:16px;color:var(--label);width:300px;text-align:center}

  /* front */
  .spa-photo{position:absolute;left:0;top:0;width:592px;height:500px;
    background:radial-gradient(ellipse at 60% 55%,#c99a78 0%,#8a5a3a 35%,#5a3520 70%,#3b2212 100%)}
  .shapes{position:absolute;left:0;top:0}
  .brand{position:absolute;left:360px;top:28px;color:var(--white);font-weight:600;font-size:30px;line-height:32px;letter-spacing:0.5px}
  .brand-dot{display:inline-block;width:14px;height:14px;border-radius:50%;background:var(--white);margin-right:8px;vertical-align:middle}
  .brand-rule{position:absolute;left:378px;top:92px;width:214px;height:2px;background:var(--white)}
  .tagline{position:absolute;right:37px;top:106px;color:var(--white);font-size:12.5px;line-height:16px;text-align:right;text-transform:uppercase}
  .tagline b{font-weight:800}
  .title-block{position:absolute;left:105px;top:378px;transform:rotate(-11deg);transform-origin:left top;color:var(--white);text-align:center;width:420px}
  .title{font-weight:800;font-size:27px;line-height:30px;letter-spacing:-0.3px}
  .subtitle{font-weight:800;font-size:14px;line-height:16px}
  .dates{position:absolute;left:0;width:592px;top:466px;text-align:center;font-size:13px;font-weight:600}
  .dates b{font-size:15px;font-weight:800}
  .intro{position:absolute;left:30px;width:532px;top:495px;text-align:center;font-weight:700;font-size:10.5px;line-height:13px;text-transform:uppercase}
  .intro strong{display:block;font-size:12.5px;line-height:15px;font-weight:800}
  .col{position:absolute;font-size:10.6px;line-height:12.8px;text-align:justify}
  .col-left{left:35px;width:252px;top:541px}
  .col-left::first-letter{font-weight:800;font-size:13px}
  .divider{position:absolute;left:297px;top:545px;width:2px;height:122px;background:var(--ink)}
  .col-right{left:306px;width:251px;top:549px}
  .col-right h3{font-size:12.5px;font-weight:700;text-align:left;margin-bottom:12px}
  .audience{position:absolute;left:35px;width:525px;top:678px;font-size:10.6px;line-height:12.6px}
  .audience h4{font-size:12.5px;font-weight:700;margin-bottom:1px}
  .audience b{font-weight:700;font-size:11.5px}
  .audience .note{font-size:9.6px;line-height:11.5px;margin-top:1px}
  .pto{position:absolute;left:507px;top:797px;width:48px;height:16px;border-radius:4px;background:var(--orange-deep);color:var(--white);font-size:8.5px;font-weight:700;text-align:center;line-height:16px}

  /* back */
  .water-photo{position:absolute;left:0;top:0;width:588px;height:556px;
    background:radial-gradient(ellipse at 55% 45%,#d9a98c 0%,#c98a6c 35%,#e9cfc0 70%,#ffffff 100%)}
  .fees{position:absolute;left:40px;top:572px;width:520px;color:var(--white);font-family:"Noto Sans",sans-serif;font-size:11.5px;line-height:15.5px}
  .fees h2{font-size:15px;font-weight:700;margin-bottom:8px;letter-spacing:0.3px}
  .fees .big{font-size:14px;font-weight:700}
  .fees p{margin-bottom:0}
  .fees .gap{margin-top:6px}
  .visit-band{position:absolute;left:0;top:748px;width:588px;height:38px;background:var(--orange);color:var(--white);text-align:center;font-family:"Noto Sans",sans-serif;font-size:11px;line-height:14px;padding-top:4px}
  .visit-band strong{font-size:14px;letter-spacing:0.4px}
</style>
</head>
<body>

<section class="panel front">
  <div class="spa-photo" role="img" aria-label="Photograph of a woman receiving a hot stone massage beside candles on a wooden spa mat"></div>

  <svg class="shapes" width="592" height="836" viewBox="0 0 592 836" aria-hidden="true">
    <polygon points="0,455 592,388 592,488 0,488" fill="var(--orange-deep)"/>
    <polygon points="0,445 518,333 547,403 0,480" fill="var(--red)"/>
  </svg>

  <div class="brand"><span class="brand-dot"></span>Silver Fern<br>Gatherings</div>
  <div class="brand-rule"></div>
  <div class="tagline">Professional<br>development<br>in a <b>retreat</b> setting</div>

  <div class="title-block">
    <div class="title">“BALI HARVEST &amp; STILLNESS”</div>
    <div class="subtitle">BUDDHISM – MINDFULNESS – HYPNOSIS</div>
  </div>

  <div class="dates">CORAL POND LODGES BALI &nbsp;<b>29 MARCH – 1 APRIL 2013</b></div>

  <div class="intro">A professional development retreat over 3 and half days exploring
    <strong>The Buddhist approach to mindfulness<br>and complementary practices.</strong></div>

  <p class="col col-left">This retreat introduces and explores at a professional level cognitive strategies [or tools] that can be applied in day-to-day living for use in therapeutic and non-therapeutic environments. Gain deep understandings and insights into handling life's challanges and embracing personal growth from practices grounded in history and supported by modern research. Leave with resources and tools that can be taken home for continuous improvement.</p>
  <div class="divider"></div>
  <div class="col col-right">
    <h3>Coral Pond Lodges Bali</h3>
    <p>A boutique resort tailored to travellers and groups, who seek to retreat, reflect, revive and renew. Coral Pond Lodges creates the ideal environment for a life changing experience. A haven of tranquil seclusion: It is the perfect location for relaxation, introspection and transformation.</p>
  </div>

  <div class="audience">
    <h4>The retreat is for :</h4>
    <p><b>Health professionals and Practitioners</b> intersted in new tools and strategies for themselves and their clients.</p>
    <p><b>Other Professionals</b> wishing to broaden their professional development and personal learning opportunities.</p>
    <p><b>Individuals</b> seeking to experience the effects of such techniques and take them home for continuous self-improvements.</p>
    <p class="note"><b>Note:</b> Depending on your professional background this course may qualify as a tax deductible item in line with continued professional development requirements.</p>
  </div>
  <div class="pto">P.T.O</div>
</section>

<section class="panel back">
  <div class="water-photo" role="img" aria-label="Photograph of water splashing over a relaxed woman with closed eyes"></div>
  <div class="fees">
    <h2>FEES AND INCLUSIONS:</h2>
    <p><span class="big">Cost: $1850</span> incl. GST,</p>
    <p>*accommodation, *meals and massage - Spaces limited to 14 people.</p>
    <p>Save 10% early Bird Special [Pay $1665 if booked before 1st of feb. 2013]</p>
    <p>and an additional 10% [ Pay $1480 ] if you bring a friend.</p>
    <p class="gap">*Includes 4 nights accommodation, materials, all breakfasts &amp; lunches as well as</p>
    <p>1 final night group dinner in one of Ubud's boutique restaurants.</p>
    <p><span class="big">Deposit: $500.</span> Booking are transferable, however deposit is non-refundable.</p>
  </div>
  <div class="visit-band">For a full course outline, more info and registration<br><strong>visit: www.silver-fern-gatherings.com</strong></div>
</section>

<div class="side-label" style="left:112px"># Front side</div>
<div class="side-label" style="left:766px"># Back side</div>

</body>
</html>
```